Vantix 220 for iPad

We are looking to design a page for the mobile app. The app is intended for financial professionals and is based on a successful desktop application. The existing design will serve as a very rough guideline, but we are open to hearing ideas.
Uploaded file #1 contains a screenshot of the existing design. The workflow is as follows:
The user picks a portfolio from the Dropdown below portfolio.
The user picks a Loss Threshold, which will dictate what gets onto the bubble chart below.
Once the bubble on the chart is clicked, a text box pops up with the description of the particular crisis that the bubble represents.
Once the bubble is clicked, the right hand side bar charts are populated with moves relevant to this scenario.
The left hand pane contains two text boxes. The lower one is particularly important, because the user is able to remove scenarios or add scenarios (screen #2). Removing scenarios is simple.
Adding scenarios brings up a wizard (screen #3). It also needs to be designed consistently with the front page of the app. The wizard has different clickable categories going down the column on the left and in a row on the top. The user can pick some or all of these categories.

Notes: The app should be designed for landscape mode only. The key to keep in mind is how the user will select bubbles on the chart. Right now, it is quite easy, but with the touchscreen it may be more complicated, so please keep that in mind when designing the chart (it should still be some version of the similar chart).
*As a first pass, please submit your idea of the concept (layout/colors/buttons) without the detailed design. We will choose 1-3 concepts and then the detailed work will take place with a much higher chance of a payout.
Updates

Thank you for the first two sketches. The second one by bertrand appears to be a bit more mobile app oriented, though we are still considering both and waiting for other submissions. One request, could you rework the sketches to include a bit more of dark blue as a background?  \

Bertrand, I think that the bubbles are too small and they are missing some volume effects. Could you make them a bit more prominent (and pick some form of dark blue background) and change the color to see if they will stand out better?
 

Industry/Entity Type

Financial

Requirements
Must have
• The general outline for the bubble chart must be retained. But the actual execution may differ significantly. We are open to seeing different ideas.
The winning design will also get a contract to design the rest of the application (2 more screens), which will be worth the same as the original design.

```html
<!DOCTYPE html>
<html lang="en">
<head>
<meta charset="utf-8">
<title>Vantix 220 – Scenario Screens</title>
<link rel="stylesheet" href="https://fonts.googleapis.com/css2?family=Ubuntu:wght@400;500&display=swap">
<style>
  :root {
    --page-bg: #e8e9ea;
    --screen-bg: #17181a;
    --screen-edge: #2a2b2e;
    --tabbar-bg: #111214;
    --tab-active: #24262a;
    --text-main: #f1f2f4;
    --text-muted: #8d9096;
    --field-bg: #0f1011;
    --field-border: #26282b;
    --accent-blue: #4a8fd6;
    --accent-blue-dark: #2d6db5;
    --accent-orange: #e0662c;
    --bubble-gold: #c98a2a;
    --grid-line: #232529;
    --plot-bg: #141517;
    --scroll-thumb: #d9dadc;
    --scroll-track: #222326;
  }
  * { box-sizing: border-box; margin: 0; padding: 0; }
  html, body { width: 1200px; height: 2264px; overflow: hidden; }
  body {
    background: var(--page-bg);
    font-family: "Ubuntu", sans-serif;
    color: var(--text-main);
    position: relative;
  }
  .screen {
    position: absolute;
    left: 238px;
    width: 724px;
    height: 418px;
    background: var(--screen-bg);
    border: 2px solid var(--screen-edge);
    border-radius: 6px;
    overflow: hidden;
  }
  .screen--select { top: 103px; }
  .screen--chart { top: 646px; }
  .screen--detail { top: 1185px; }
  .screen--details { top: 1728px; }

  .tabbar {
    position: absolute; left: 0; top: 0; width: 100%; height: 58px;
    background: var(--tabbar-bg);
  }
  .back-btn {
    position: absolute; left: 17px; top: 16px; width: 88px; height: 32px;
    background: linear-gradient(#5fa0e0, var(--accent-blue-dark));
    border-radius: 3px;
    font-size: 11px; color: #163e6b; letter-spacing: .5px;
    display: flex; align-items: center; padding-left: 12px; gap: 10px;
  }
  .back-btn::before {
    content: ""; border: 5px solid transparent; border-right: 6px solid #163e6b; border-left: 0;
  }
  .tab {
    position: absolute; top: 14px; height: 44px;
    display: flex; align-items: center; justify-content: center;
    font-size: 19px; color: var(--text-main); border-radius: 3px 3px 0 0;
  }
  .tab--select { left: 116px; width: 216px; }
  .tab--charts { left: 340px; width: 113px; }
  .tab--details { left: 460px; width: 128px; }
  .tab.is-active { background: var(--tab-active); }

  .scrollbar {
    position: absolute; width: 4px; background: var(--scroll-track); border-radius: 2px;
  }
  .scrollbar span {
    display: block; width: 4px; background: var(--scroll-thumb); border-radius: 2px;
  }

  /* Select portfolio form */
  .form-row { position: absolute; left: 0; width: 560px; height: 34px; display: flex; align-items: center; }
  .form-label { width: 228px; text-align: right; font-size: 15px; color: #d8d9dc; }
  .select {
    position: absolute; left: 241px; width: 277px; height: 34px;
    background: var(--field-bg); border: 1px solid var(--field-border); border-radius: 2px;
    font-size: 15px; display: flex; align-items: center; padding-left: 18px;
  }
  .select::after {
    content: ""; position: absolute; right: 8px; top: 7px; width: 19px; height: 19px;
    background: linear-gradient(#f2f2f2, #b9babc); border-radius: 2px;
  }
  .select::before {
    content: ""; position: absolute; right: 13px; top: 14px; z-index: 1;
    border: 5px solid transparent; border-top: 6px solid #333; border-bottom: 0;
  }
  .stepper { position: absolute; left: 241px; height: 34px; display: flex; align-items: center; gap: 0;
    background: var(--field-bg); border: 1px solid var(--field-border); border-radius: 2px; padding: 0 4px; }
  .stepper-btn { width: 24px; height: 24px; background: linear-gradient(#f2f2f2, #b9babc); border-radius: 2px;
    color: #222; font-size: 18px; display: flex; align-items: center; justify-content: center; }
  .stepper-value { width: 44px; text-align: center; font-size: 15px; }
  .check { position: absolute; left: 246px; top: 362px; display: flex; align-items: center; gap: 12px; font-size: 15px; color: #d8d9dc; }
  .check-box { width: 10px; height: 10px; background: var(--accent-blue); border-radius: 1px; box-shadow: 0 0 0 3px #0f1011; }

  /* Charts */
  .plot { position: absolute; }
  .axis-y { position: absolute; font-size: 14px; color: #d8d9dc; transform: rotate(-90deg); transform-origin: center; white-space: nowrap; }
  .axis-x { position: absolute; font-size: 14px; color: #d8d9dc; }

  .scenario-panel { position: absolute; left: 523px; top: 72px; width: 190px; }
  .scenario-title { font-size: 17px; margin-bottom: 14px; }
  .scenario-metric { display: flex; gap: 10px; font-size: 14px; margin-bottom: 12px; line-height: 1.35; }
  .scenario-metric b { font-weight: 500; width: 52px; text-align: right; flex: none; }
  .scenario-metric span { color: var(--text-muted); }

  /* Details */
  .contrib { position: absolute; top: 66px; width: 282px; }
  .contrib--high { left: 27px; }
  .contrib--low { left: 333px; }
  .contrib-title { font-size: 18px; margin-bottom: 16px; }
  .contrib-row { position: relative; height: 34px; border-bottom: 1px solid #222428; display: flex; justify-content: space-between; align-items: flex-start; padding-top: 2px; font-size: 14px; width: 270px; }
  .contrib-row .name { color: var(--text-muted); }
  .contrib-row .bar { position: absolute; bottom: 3px; height: 3px; border-radius: 1px; }
  .contrib--high .bar { left: 2px; background: var(--accent-blue); }
  .contrib--low .bar { right: 2px; background: var(--accent-orange); }
</style>
</head>
<body>

<svg width="0" height="0" style="position:absolute" aria-hidden="true">
  <defs>
    <radialGradient id="bubble-blue" cx="40%" cy="35%" r="65%">
      <stop offset="0" stop-color="#6fb2f0"/>
      <stop offset=".6" stop-color="#2a78cc"/>
      <stop offset="1" stop-color="#164f92"/>
    </radialGradient>
    <radialGradient id="bubble-gold" cx="40%" cy="35%" r="65%">
      <stop offset="0" stop-color="#f0b54a"/>
      <stop offset=".7" stop-color="#c98a2a"/>
      <stop offset="1" stop-color="#8c5c16"/>
    </radialGradient>
    <pattern id="grid" width="14" height="14" patternUnits="userSpaceOnUse">
      <path d="M14 0H0V14" fill="none" stroke="#24262a" stroke-width="1"/>
    </pattern>
  </defs>
</svg>

<!-- Screen 1: select portfolio -->
<section class="screen screen--select">
  <nav class="tabbar">
    <div class="back-btn">BACK</div>
    <div class="tab tab--select is-active">SELECT PORTFOLIO</div>
    <div class="tab tab--charts">CHARTS</div>
    <div class="tab tab--details">DETAILS</div>
  </nav>
  <div class="form-row" style="top:76px"><span class="form-label">Portfolio Date</span><div class="select">Portfolio Date</div></div>
  <div class="form-row" style="top:124px"><span class="form-label">Portfolio</span><div class="select">Select Portfolio</div></div>
  <div class="form-row" style="top:172px"><span class="form-label">Currency</span><div class="select">USD</div></div>
  <div class="form-row" style="top:219px"><span class="form-label">Weight Type</span><div class="select">Active</div></div>
  <div class="form-row" style="top:265px"><span class="form-label">Model</span><div class="select">Quantora</div></div>
  <div class="form-row" style="top:313px"><span class="form-label">Loss Threshold</span>
    <div class="stepper"><span class="stepper-btn">−</span><span class="stepper-value">-10</span><span class="stepper-btn">+</span></div>
  </div>
  <div class="check"><span class="check-box"></span>Only Key Scenarios</div>
  <div class="scrollbar" style="left:700px;top:74px;height:320px"><span style="height:200px"></span></div>
</section>

<!-- Screen 2: chart overview -->
<section class="screen screen--chart">
  <nav class="tabbar">
    <div class="back-btn">BACK</div>
    <div class="tab tab--select">SELECT PORTFOLIO</div>
    <div class="tab tab--charts is-active">CHARTS</div>
    <div class="tab tab--details">DETAILS</div>
  </nav>
  <svg class="plot" style="left:0;top:0" width="724" height="418" role="img" aria-label="Scenario bubble chart of loss against correlation surprise">
    <rect x="48" y="63" width="658" height="302" fill="var(--plot-bg)"/>
    <rect x="48" y="63" width="658" height="302" fill="url(#grid)"/>
    <path d="M47 107 l9 -6 v12z" fill="var(--accent-blue)"/>
    <path d="M47 224 l9 -6 v12z" fill="var(--bubble-gold)"/>
    <circle cx="473" cy="104" r="12" fill="#c98a2a" opacity=".25"/>
    <circle cx="473" cy="104" r="6" fill="url(#bubble-gold)"/>
    <circle cx="175" cy="275" r="12" fill="#c98a2a" opacity=".25"/>
    <circle cx="175" cy="275" r="6" fill="url(#bubble-gold)"/>
    <circle cx="249" cy="154" r="6" fill="url(#bubble-blue)"/>
    <circle cx="593" cy="154" r="6" fill="url(#bubble-blue)"/>
    <circle cx="415" cy="282" r="6" fill="url(#bubble-blue)"/>
  </svg>
  <div class="axis-y" style="left:-37px;top:205px">Correlation Surprise</div>
  <div class="axis-x" style="left:260px;top:378px">Loss</div>
</section>

<!-- Screen 3: chart with selected scenario -->
<section class="screen screen--detail">
  <nav class="tabbar">
    <div class="back-btn">BACK</div>
    <div class="tab tab--select">SELECT PORTFOLIO</div>
    <div class="tab tab--charts is-active">CHARTS</div>
    <div class="tab tab--details">DETAILS</div>
  </nav>
  <svg class="plot" style="left:0;top:0" width="520" height="418" role="img" aria-label="Scenario bubble chart with the selected scenario enlarged">
    <rect x="47" y="60" width="466" height="307" rx="3" fill="var(--plot-bg)"/>
    <rect x="47" y="60" width="466" height="307" fill="url(#grid)"/>
    <path d="M51 113 l9 -6 v12z" fill="var(--accent-blue)"/>
    <path d="M51 229 l9 -6 v12z" fill="var(--bubble-gold)"/>
    <circle cx="472" cy="106" r="12" fill="#c98a2a" opacity=".25"/>
    <circle cx="472" cy="106" r="6" fill="url(#bubble-gold)"/>
    <circle cx="198" cy="125" r="17" fill="url(#bubble-blue)"/>
    <circle cx="415" cy="284" r="6" fill="url(#bubble-blue)"/>
  </svg>
  <div class="axis-y" style="left:-37px;top:205px">Correlation Surprise</div>
  <div class="axis-x" style="left:258px;top:380px">Loss</div>
  <aside class="scenario-panel">
    <h2 class="scenario-title">Stagflation Server</h2>
    <div class="scenario-metric"><b>-18.82</b><span>Loss</span></div>
    <div class="scenario-metric"><b>0.00</b><span>Plausibility</span></div>
    <div class="scenario-metric"><b>-18.82</b><span>Correlation<br>Surprise</span></div>
  </aside>
  <div class="scrollbar" style="left:707px;top:120px;height:175px"><span style="height:175px"></span></div>
</section>

<!-- Screen 4: details -->
<section class="screen screen--details">
  <nav class="tabbar">
    <div class="back-btn">BACK</div>
    <div class="tab tab--select">SELECT PORTFOLIO</div>
    <div class="tab tab--charts">CHARTS</div>
    <div class="tab tab--details is-active">DETAILS</div>
  </nav>
  <div class="contrib contrib--high">
    <h2 class="contrib-title">Assets Contribution 10 Highest</h2>
    <div class="contrib-row"><span class="name">KRT 6.505 02/12/67</span><span>0.083</span><i class="bar" style="width:148px"></i></div>
    <div class="contrib-row"><span class="name">KRT 6.505 02/12/67</span><span>0.083</span><i class="bar" style="width:134px"></i></div>
    <div class="contrib-row"><span class="name">KRT 6.505 02/12/67</span><span>0.083</span><i class="bar" style="width:80px"></i></div>
    <div class="contrib-row"><span class="name">KRT 6.505 02/12/67</span><span>0.083</span><i class="bar" style="width:77px"></i></div>
    <div class="contrib-row"><span class="name">KRT 6.505 02/12/67</span><span>0.083</span><i class="bar" style="width:66px"></i></div>
    <div class="contrib-row"><span class="name">KRT 6.505 02/12/67</span><span>0.083</span><i class="bar" style="width:46px"></i></div>
    <div class="contrib-row"><span class="name">KRT 6.505 02/12/67</span><span>0.083</span><i class="bar" style="width:44px"></i></div>
    <div class="contrib-row"><span class="name">KRT 6.505 02/12/67</span><span>0.083</span><i class="bar" style="width:33px"></i></div>
  </div>
  <div class="contrib contrib--low">
    <h2 class="contrib-title">Assets Contribution 10 Lowest</h2>
    <div class="contrib-row"><span class="name">KRT 6.505 02/12/67</span><span>0.083</span><i class="bar" style="width:190px"></i></div>
    <div class="contrib-row"><span class="name">KRT 6.505 02/12/67</span><span>0.083</span><i class="bar" style="width:218px"></i></div>
    <div class="contrib-row"><span class="name">KRT 6.505 02/12/67</span><span>0.083</span><i class="bar" style="width:160px"></i></div>
    <div class="contrib-row"><span class="name">KRT 6.505 02/12/67</span><span>0.083</span><i class="bar" style="width:130px"></i></div>
    <div class="contrib-row"><span class="name">KRT 6.505 02/12/67</span><span>0.083</span><i class="bar" style="width:84px"></i></div>
    <div class="contrib-row"><span class="name">KRT 6.505 02/12/67</span><span>0.083</span><i class="bar" style="width:60px"></i></div>
    <div class="contrib-row"><span class="name">KRT 6.505 02/12/67</span><span>0.083</span><i class="bar" style="width:58px"></i></div>
    <div class="contrib-row"><span class="name">KRT 6.505 02/12/67</span><span>0.083</span><i class="bar" style="width:40px"></i></div>
  </div>
  <div class="scrollbar" style="left:303px;top:110px;height:286px"><span style="height:180px"></span></div>
  <div class="scrollbar" style="left:613px;top:110px;height:286px"><span style="height:180px"></span></div>
</section>

</body>
</html>
```